Flyer for American Indian Elders on Dementia Warning Signs

We need a flyer designed for older adults who are American Indian or Alaska Native (in the U.S.).

Ideally, the flyer should complement the colors of our logos. The project logo and our organization logo are attached to the brief.

When people see the flyer we want them to feel that it represents their culture, is warm, and professional but relatable to older adults and people who have limited incomes.

I have attached an earlier draft of the document we designed ourselves BUT we want different and better.

It is for older adults who have trouble reading so:
1. you must use a font that is 11.5 points or larger
2. Do not put text over complex pictures or use shading with words
3. You can use a serif font for the heading, but should use san serif for the body text
4. There should be good contrast between the font color and background

Please do not use any images that include a head dress or pictures of American Indian people or things that are very traditional or "token" imagery.

We need to save a small space under the call out box/ somewhere on the flyer for other people to add their logo once they download.

Let us know if you have questions or need additional information.

Target Market(s)

Older American Indian people

Font styles to use
Serif
Sans Serif

Requirements
Must have
• Easy to read for older adults
Should not have
• indian headdress

```html
<!DOCTYPE html>
<html lang="en">
<head>
<meta charset="utf-8">
<title>10 Signs of Thinking or Memory Changes That Might Be Dementia</title>
<link rel="stylesheet" href="https://fonts.googleapis.com/css2?family=Montserrat:wght@700;800&family=Roboto:wght@400;500;700&display=swap">
<style>
  :root {
    --clay: #a85a55;
    --clay-deep: #9c4f4a;
    --callout: #b3625c;
    --teal: #4ea9b1;
    --teal-soft: #5aa7ad;
    --ink: #222222;
    --paper: #ffffff;
    --backdrop: #b1b0b1;
  }
  * { box-sizing: border-box; margin: 0; padding: 0; }
  html, body { width: 960px; height: 1200px; overflow: hidden; }
  body {
    background: var(--backdrop);
    font-family: "Roboto", Arial, sans-serif;
    color: var(--ink);
    position: relative;
  }
  .flyer {
    position: absolute;
    left: 70px; top: 20px;
    width: 820px; height: 1160px;
    background: var(--paper);
    overflow: hidden;
  }
  .flyer-art { position: absolute; inset: 0; width: 820px; height: 1160px; }
  .title {
    position: absolute; left: 0; right: 0; top: 14px;
    text-align: center; color: var(--paper);
    font-family: "Montserrat", Arial, sans-serif; font-weight: 800;
  }
  .title-main { display: block; font-size: 50px; line-height: 52px; letter-spacing: 0.5px; }
  .title-sub { display: block; font-size: 28px; line-height: 32px; font-weight: 700; }
  .intro {
    position: absolute; left: 45px; width: 745px; top: 140px;
    font-size: 15.5px; line-height: 19.5px;
  }
  .intro p + p { margin-top: 7px; }
  .timeline { position: absolute; width: 1.5px; background: var(--clay); }
  .sign { position: absolute; }
  .sign-num {
    position: absolute; left: -34px; top: 0;
    width: 24px; height: 24px; border-radius: 50%;
    background: var(--clay); color: var(--paper);
    font-weight: 700; font-size: 13px; line-height: 24px; text-align: center;
  }
  .sign-num.wide { font-size: 11px; }
  .sign-title {
    color: var(--clay); font-weight: 700; font-size: 15.5px; line-height: 19px;
    text-transform: uppercase;
  }
  .sign-list { list-style: none; margin-top: 5px; font-size: 15.5px; line-height: 19px; }
  .sign-list li { position: relative; padding-left: 21px; }
  .sign-list li::before {
    content: ""; position: absolute; left: 2px; top: 6px;
    width: 7px; height: 7px; border-radius: 50%; background: var(--teal-soft);
  }
  .sign-text { margin-top: 10px; font-size: 15.5px; line-height: 19px; }
  .col-left { left: 79px; width: 350px; }
  .col-right { left: 474px; width: 330px; }
  .callout {
    position: absolute; left: 440px; top: 784px; width: 355px;
    background: var(--callout); border-radius: 5px;
    color: var(--paper); padding: 13px 10px 6px 14px;
  }
  .callout ul { list-style: none; font-size: 15px; line-height: 19px; }
  .callout li { position: relative; padding-left: 26px; margin-bottom: 6px; }
  .callout li svg { position: absolute; left: 0; top: 3px; }
  .callout li.strong { font-weight: 700; }
  .partners { position: absolute; left: 45px; top: 876px; width: 360px; }
  .partner {
    display: flex; align-items: center; gap: 12px;
    font-weight: 700; font-size: 22px; line-height: 25px;
  }
  .partner + .partner { margin-top: 30px; }
  .partner-council { color: var(--clay); }
  .partner-network { color: var(--teal); }
  .partner-mark { flex: none; width: 66px; height: 66px; border-radius: 50%; background: var(--teal); }
  .learn-more {
    position: absolute; left: 440px; width: 355px; top: 1046px;
    text-align: center; color: var(--paper);
  }
  .learn-more p { font-size: 15.5px; line-height: 19px; }
  .learn-more .links { margin-top: 6px; font-weight: 700; font-size: 22px; line-height: 26px; }
</style>
</head>
<body>
<main class="flyer">
  <svg class="flyer-art" viewBox="0 0 820 1160" aria-hidden="true">
    <defs>
      <linearGradient id="band" x1="0" y1="0" x2="1" y2="0">
        <stop offset="0" stop-color="#a85a55"/>
        <stop offset="0.55" stop-color="#967a78"/>
        <stop offset="1" stop-color="#4ea9b1"/>
      </linearGradient>
      <linearGradient id="base" x1="0" y1="1" x2="1" y2="0">
        <stop offset="0" stop-color="#a85a55"/>
        <stop offset="0.45" stop-color="#7f9094"/>
        <stop offset="0.75" stop-color="#4ea9b1"/>
        <stop offset="1" stop-color="#4ea9b1"/>
      </linearGradient>
    </defs>
    <path d="M0 0 H820 V104 C 640 132 480 118 300 114 C 170 112 70 124 0 156 Z" fill="url(#band)"/>
    <path d="M0 156 C 70 124 170 112 300 114 C 480 118 640 132 820 104 V110 C 640 138 480 124 300 120 C 180 118 80 128 0 162 Z" fill="#4ea9b1" opacity="0.9"/>
    <path d="M820 886 C 690 874 540 920 430 1010 C 330 1090 190 1140 0 1110 V1160 H820 Z" fill="url(#base)"/>
    <path d="M820 878 C 690 864 540 910 426 1002 L430 1010 C 540 920 690 874 820 890 Z" fill="#a85a55"/>
  </svg>

  <h1 class="title">
    <span class="title-main">10 SIGNS OF THINKING OR</span>
    <span class="title-sub">MEMORY CHANGES THAT MIGHT BE DEMENTIA</span>
  </h1>

  <div class="intro">
    <p>As we get older, we may slow down a bit. This is a normal part of aging. Changes in memory or thinking that make it harder to get through the day, are not a normal part of aging. These may be early signs of dementia.</p>
    <p>Because American Indian and Alaska Native people have a high risk of dementia, it is important to know the warning signs. Do you have any of these 10 signs? If so, talk to your doctor.</p>
  </div>

  <div class="timeline" style="left:56px; top:272px; height:592px;"></div>
  <div class="timeline" style="left:451px; top:272px; height:590px;"></div>

  <section class="sign col-left" style="top:270px;">
    <span class="sign-num">1</span>
    <h2 class="sign-title">Memory loss that affects your daily life. You may</h2>
    <ul class="sign-list">
      <li>Forget events or important dates</li>
      <li>Repeat yourself</li>
      <li>Rely more often on lists or sticky notes to remember things</li>
    </ul>
  </section>

  <section class="sign col-left" style="top:400px;">
    <span class="sign-num">2</span>
    <h2 class="sign-title">Trouble planning or solving problems. You may have a harder time:</h2>
    <ul class="sign-list">
      <li>Paying bills</li>
      <li>Cooking recipes you have used for years</li>
    </ul>
  </section>

  <section class="sign col-left" style="top:513px;">
    <span class="sign-num">3</span>
    <h2 class="sign-title">Get confused about the time, date, or where you are.</h2>
  </section>

  <section class="sign col-left" style="top:564px;">
    <span class="sign-num">4</span>
    <h2 class="sign-title">Daily tasks are getting harder, including:</h2>
    <ul class="sign-list">
      <li>Driving</li>
      <li>Making a grocery list or going shopping</li>
    </ul>
  </section>

  <section class="sign col-left" style="top:656px;">
    <span class="sign-num">5</span>
    <h2 class="sign-title">Trouble with how your eyesight &amp; thinking work together that gets worse. This includes:</h2>
    <ul class="sign-list" style="margin-top:10px;">
      <li>Tripping, falls, or problems with your balance</li>
      <li>Spilling or dropping things more</li>
    </ul>
  </section>

  <section class="sign col-left" style="top:770px;">
    <span class="sign-num">6</span>
    <h2 class="sign-title">New trouble talking or writing.</h2>
    <p class="sign-text">You have a hard time finding the words you want to say. For example, you may say “that thing on your wrist that tells time” instead of “watch.”</p>
  </section>

  <section class="sign col-right" style="top:270px;">
    <span class="sign-num">7</span>
    <h2 class="sign-title">Lose and cannot find things. For example, you:</h2>
    <ul class="sign-list">
      <li>Can’t find the coffee pot that you use every day</li>
      <li>Might put your car keys in the freezer</li>
    </ul>
  </section>

  <section class="sign col-right" style="top:383px;">
    <span class="sign-num">8</span>
    <h2 class="sign-title">Notice changes in your mood or personality, such as being</h2>
    <ul class="sign-list">
      <li>Easily mad or sad in everyday situations</li>
      <li>More fearful (scared) or suspicious (not trusting)</li>
    </ul>
  </section>

  <section class="sign col-right" style="top:491px;">
    <span class="sign-num">9</span>
    <h2 class="sign-title">Act different and make poor choices. This may make you more likely to:</h2>
    <ul class="sign-list">
      <li>Spend money you do not have or be a scam victim</li>
      <li>Stop washing up regularly or pay less attention to how you look</li>
      <li>Forget to take care of your pet</li>
    </ul>
  </section>

  <section class="sign col-right" style="top:655px;">
    <span class="sign-num wide">10</span>
    <h2 class="sign-title">Pull away from friends and family because it is harder to keep up.</h2>
    <ul class="sign-list" style="margin-top:10px;">
      <li>You may not want to do things you used to enjoy, like sporting events, church, music, or sex.</li>
    </ul>
  </section>

  <aside class="callout">
    <ul>
      <li><svg width="16" height="16" viewBox="0 0 16 16"><circle cx="8" cy="8" r="8" fill="#fff"/><path d="M4.5 8.2 L7 10.6 L11.5 5.8" stroke="#b3625c" stroke-width="2" fill="none"/></svg>American Indian &amp; Alaska Native people have a higher risk of dementia than White people.</li>
      <li><svg width="16" height="16" viewBox="0 0 16 16"><circle cx="8" cy="8" r="8" fill="#fff"/><path d="M4.5 8.2 L7 10.6 L11.5 5.8" stroke="#b3625c" stroke-width="2" fill="none"/></svg>Big changes in memory or thinking that make it hard to get through the day are not a normal part of aging.</li>
      <li><svg width="16" height="16" viewBox="0 0 16 16"><circle cx="8" cy="8" r="8" fill="#fff"/><path d="M4.5 8.2 L7 10.6 L11.5 5.8" stroke="#b3625c" stroke-width="2" fill="none"/></svg>People with one or more of these 10 signs should talk to their doctor to find the cause. It is not always dementia.</li>
      <li class="strong"><svg width="16" height="16" viewBox="0 0 16 16"><circle cx="8" cy="8" r="8" fill="#fff"/><path d="M4.5 8.2 L7 10.6 L11.5 5.8" stroke="#b3625c" stroke-width="2" fill="none"/></svg>Early dementia diagnosis gives you a chance to get care &amp; plan your future.</li>
    </ul>
  </aside>

  <div class="partners">
    <div class="partner partner-council">Council on Native Elder Wellness</div>
    <div class="partner partner-network"><span class="partner-mark"></span>Tribal Brain Health Resource Network</div>
  </div>

  <div class="learn-more">
    <p>To learn more about the warning signs of dementia in American Indian and Alaska Native people, visit:</p>
    <p class="links">www.TribalMindWellness.org<br>www.elderhealthinfo.org/aging</p>
  </div>
</main>
</body>
</html>
```